Firmenflyer
Zielgruppe
Ausschließlich öffentliche Verwaltungen wie Gemeinden, Städte und Landratsämter
Aufgabenstellung
Ein Vorstellungs- und Überblick-Flyer. Es soll kurz enthalten sein wo wir tätig sein, was wir machen. Eine Seite sollte unseren noch nicht veröffentlichten Kauf-Shop bewerben in dem Software geordert werden kann.
Format sollte A5 Quer mit Falz sein

```html
<!DOCTYPE html>
<html lang="de">
<head>
<meta charset="utf-8">
<title>Verwano – Firmenflyer</title>
<link rel="stylesheet" href="https://fonts.googleapis.com/css2?family=Source+Sans+3:wght@400;600;700&display=swap">
<style>
:root{
  --brown:#8a4a1f;
  --brown-dark:#5b3418;
  --ink:#4a4543;
  --quote:#ebe5df;
  --paper:#ffffff;
}
*{box-sizing:border-box;margin:0;padding:0}
html,body{width:1200px;height:1200px;overflow:hidden;background:var(--paper)}
body{position:relative;font-family:"Source Sans 3",Arial,sans-serif;color:var(--ink)}
.sheet{position:absolute;background:var(--paper);overflow:hidden;box-shadow:0 2px 6px rgba(0,0,0,.18)}
.sheet--inside{left:173px;top:466px;width:1002px;height:709px;z-index:1}
.sheet--outside{left:21px;top:21px;width:1004px;height:708px;z-index:2}
.photo{position:absolute}
.body-text{position:absolute;z-index:2;font-size:9.6px;line-height:13px}
.body-text p+p{margin-top:8px}
.accent{color:var(--brown);font-weight:700}
.heading{position:absolute;z-index:2;font-weight:400;color:var(--ink);font-size:26px;line-height:1;letter-spacing:-.2px;white-space:nowrap}
.quote{position:absolute;z-index:1;width:52px;height:52px;fill:var(--quote)}
.logo-box{position:absolute;z-index:2;background:var(--paper);border:1.5px solid var(--brown);border-bottom:none;border-radius:14px 14px 0 0;display:flex;align-items:center;justify-content:center;gap:8px}
.logo-mark{width:16px;height:16px;background:var(--brown)}
.logo-name{font-size:26px;font-weight:700;color:var(--brown)}
.panel-right-bg{position:absolute;left:500px;top:0;width:502px;height:709px;background:linear-gradient(90deg,#f1efed,#ffffff 40%,#f4f2f0)}
.band-top{position:absolute;left:500px;top:0;width:502px;height:26px;background:var(--brown)}
.band-thin{position:absolute;left:500px;top:655px;width:502px;height:8px;background:var(--brown-dark)}
.band-bottom{position:absolute;left:500px;top:667px;width:502px;height:42px;background:var(--brown)}
.tile{position:absolute;width:212px;height:210px;border-radius:14px;background:rgba(90,70,55,.28)}
.tile--logo{background:var(--paper);display:flex;align-items:center;justify-content:center;gap:8px}
</style>
</head>
<body>

<section class="sheet sheet--inside">
  <div class="photo" style="left:0;top:0;width:254px;height:709px;background:linear-gradient(180deg,#cfc4b9 0%,#e9e3dd 45%,#d9d2cb 100%)" role="img" aria-label="Foto in Sepia: Händedruck vor einem Geländer"></div>
  <div class="logo-box" style="left:20px;top:610px;width:217px;height:99px">
    <span class="logo-mark"></span><span class="logo-name">Verwano</span>
  </div>

  <div class="body-text" style="left:283px;top:274px;width:190px">
    <p>nalverwaltung und haben zudem starke Partner im Rücken, die uns nach besten Kräften unterstützen.</p>
    <p class="accent">Sie haben Interesse an uns und unseren Produkten? Wir würden uns freuen von Ihnen zu hören.</p>
  </div>

  <svg class="quote" style="left:270px;top:392px" viewBox="0 0 52 52"><path d="M8 30h12l-8 22H2zM28 30h12l-8 22H22z"/></svg>
  <svg class="quote" style="left:420px;top:375px" viewBox="0 0 52 52"><path d="M12 0h10l-6 22H4zM32 0h10l-6 22H24z"/></svg>
  <h2 class="heading" style="right:529px;top:402px">Support</h2>
  <div class="body-text" style="left:283px;top:449px;width:190px">
    <p>An Software werden oft situationsspezifische Anforderungen gestellt, die standardisierte Software meist nicht in der Lage ist, zu erfüllen. Besonders im Bereich der öffentlichen Verwaltung ist auch die Software von vielen äußeren Einflüssen abhängig. Gesetzesänderungen auf Bundes- und EU-Ebene finden auch hier in immer schnelleren Zyklen statt. Im Bereich DMS und Sitzungsdienst steigen die Anforderungen ebenfalls stetig.</p>
    <p>Neben einer professionellen, aus Anwendersicht geschaffenen Software bieten wir zusätzlich Support bei Fragen oder Problemen im Tagesgeschäft. Dazu nutzen wir alle gängigen Kommunikationsmittel wie Telefon-Hotline, Mail-Hotline und Fernwartungstools.</p>
  </div>

  <div class="panel-right-bg"></div>
  <div class="band-top"></div>
  <svg class="quote" style="left:925px;top:48px;width:70px;height:70px" viewBox="0 0 52 52"><path d="M12 0h10l-6 22H4zM32 0h10l-6 22H24z"/></svg>
  <h2 class="heading" style="right:40px;top:80px">Branchenlösungen</h2>
  <div class="body-text" style="left:527px;top:143px;width:445px">
    <p>Unsere Fachlösungen decken die Aufgaben von Gemeinden, Städten und Landratsämtern ab. Jedes Modul ist auf die Praxis der Verwaltung abgestimmt und lässt sich schrittweise erweitern. So wächst die Software mit Ihren Anforderungen und bleibt dabei einfach zu bedienen, sicher und zuverlässig im täglichen Einsatz.</p>
    <p class="accent" style="margin-top:14px">Denken Sie auch daran, dass unsere Mitarbeiter Sie über die Hotline nur dann erfolgreich unterstützen können, wenn die erforderlichen Grundkenntnisse vorhanden sind.</p>
  </div>

  <svg class="quote" style="left:540px;top:316px" viewBox="0 0 52 52"><path d="M8 30h12l-8 22H2zM28 30h12l-8 22H22z"/></svg>
  <svg class="quote" style="left:866px;top:296px" viewBox="0 0 52 52"><path d="M12 0h10l-6 22H4zM32 0h10l-6 22H24z"/></svg>
  <h2 class="heading" style="left:593px;top:325px">Kollegen schulen Kollegen</h2>
  <div class="body-text" style="left:527px;top:373px;width:226px">
    <p>Eine gründliche Ausbildung ist die beste Voraussetzung für erfolgreiches Arbeiten. Stimmen Sie Ihren Schulungsbedarf mit unseren Mitarbeitern ab, um optimale Startbedingungen für den Einsatz der Software bei Ihnen im Amt zu schaffen. Bei Personalwechsel oder Änderungen der Aufgabenbereiche prüfen Sie bitte, ob erneuter Schulungsbedarf vorhanden ist. Beachten Sie auch unsere Vertiefungs-, Update- und Aufbauseminare. Nur eine regelmäßige Weiterbildung sichert den dauerhaft erfolgreichen Einsatz unserer Softwareprodukte und versetzt Sie in die Lage, Ihre täglich anfallende Arbeit effizient mit unseren Softwareprodukten zu erledigen.</p>
    <p class="accent">Denken Sie auch daran, dass unsere Mitarbeiter Sie über die Hotline nur dann erfolgreich unterstützen können, wenn die erforderlichen Grundkenntnisse vorhanden sind.</p>
  </div>
  <div class="photo" style="left:773px;top:367px;width:229px;height:269px;border:1.5px solid var(--brown);border-right:none;border-radius:14px 0 0 14px;background:linear-gradient(135deg,#f3efeb,#d6cbc0 70%,#b8a796)" role="img" aria-label="Foto: Schulungssituation mit Trainer und Teilnehmerinnen im Büro"></div>

  <div class="band-thin"></div>
  <div class="band-bottom"></div>
</section>

<section class="sheet sheet--outside">
  <div class="photo" style="left:0;top:0;width:500px;height:230px;background:linear-gradient(90deg,#d9cfc5,#ebe5df 50%,#c9bdb1)" role="img" aria-label="Foto in Sepia: Geschäftsmann auf einer Treppe mit Handy"></div>
  <div class="photo" style="left:246px;top:0;width:207px;height:148px;border-radius:0 0 14px 14px;background:rgba(95,75,60,.35)" role="img" aria-label="Ausschnitt: Hand mit Mobiltelefon"></div>

  <svg class="quote" style="left:22px;top:292px" viewBox="0 0 52 52"><path d="M8 30h12l-8 22H2zM28 30h12l-8 22H22z"/></svg>
  <svg class="quote" style="left:412px;top:258px" viewBox="0 0 52 52"><path d="M12 0h10l-6 22H4zM32 0h10l-6 22H24z"/></svg>
  <h1 class="heading" style="left:43px;top:280px">Mit Verwano in Verbindung setzen</h1>

  <div class="body-text" style="left:40px;top:377px;width:186px">
    <p>Im modernen Medienzeitalter können wir Ihnen eine Vielzahl von Möglichkeiten zur Kontaktaufnahme anbieten: per <b>Telefon</b> oder <b>Handy</b>, per <b>Fax</b> oder per <b>eMail</b>.</p>
    <p style="margin-top:34px">Verwano Software UG<br>(haftungsbeschränkt)<br>Lindenweg 12<br>93199 Neudorf</p>
  </div>
  <div class="body-text" style="left:264px;top:377px;width:196px">
    <p><b>Telefonisch</b> sind wir von Montag bis Donnerstag 08.00 bis 12.00 Uhr und von 13.00 bis 18.00 Uhr, Freitag 08.00 bis 12.00 Uhr und Samstag von 08.00 Uhr bis 12.00 Uhr für Sie unter der kostenfreien Rufnummer 0800/123 456-010 erreichbar.</p>
    <p>Ein <b>Fax</b> schicken Sie bitte an die kostenfreie Faxnummer 0800/123 456-020.</p>
    <p>Bei Interesse an unseren Dienstleistungen &amp; Lösungen erreichen Sie uns <b>via eMail</b> unter:</p>
    <p><b>vertrieb@verwano.de</b></p>
  </div>

  <div class="logo-box" style="left:32px;top:616px;width:212px;height:92px">
    <span class="logo-mark"></span><span class="logo-name">Verwano</span>
  </div>

  <div class="photo" style="left:500px;top:0;width:504px;height:708px;background:linear-gradient(160deg,#efeae5 0%,#cdbfb2 45%,#a8968a 100%)" role="img" aria-label="Foto in Sepia: drei lächelnde Kollegen im Gespräch"></div>
  <div class="tile" style="left:531px;top:248px"></div>
  <div class="tile" style="left:762px;top:248px"></div>
  <div class="tile" style="left:531px;top:475px"></div>
  <div class="tile tile--logo" style="left:762px;top:475px">
    <span class="logo-mark"></span><span class="logo-name">Verwano</span>
  </div>
</section>

</body>
</html>
```